Office Building Banner

Need a 4x8 vinyl banner made for our office/storage headquarters. Our branded colors and logo can be taken from our website, www.brenmarroofingtx.com. All other elements of our brand have not been decided on yet, so you have creative autonomy there. Our location faces a busy highway in Seguin, Texas, so the banner needs to have our contact information and full name clearly seen from a bit away's away, hope that makes sense. Our company wants to convey attributes of strength, loyalty, protection - basically emulating the qualities of a wolf and his pack. I have uploaded a few items we have been using to date, but as you can see, graphic design is not our forte.

```html
<!DOCTYPE html>
<html lang="en">
<head>
<meta charset="utf-8">
<title>Brenmar Roofing &amp; Renovations — Stationery Set</title>
<link rel="stylesheet" href="https://fonts.googleapis.com/css2?family=Montserrat:wght@700;800;900&family=Arimo:wght@400;700&family=Poppins:wght@400;600;700&display=swap">
<style>
  :root {
    --orange: #ff8200;
    --black: #111111;
    --ink: #1a1a1a;
    --grey-text: #6b6b6b;
    --page: #e3e3e3;
    --white: #ffffff;
    --silver-light: #f2f2f2;
    --silver-dark: #a9a9a9;
  }
  * { margin: 0; padding: 0; box-sizing: border-box; }
  html, body { width: 991px; height: 1200px; overflow: hidden; background: var(--page); }
  .canvas { position: relative; width: 991px; height: 1200px; }
  .piece { position: absolute; overflow: hidden; box-shadow: 2px 3px 6px rgba(0,0,0,.28); }
  .abs { position: absolute; }

  /* Brand name block (stand-in for the mark) */
  .brand { position: absolute; display: flex; flex-direction: column; align-items: center; text-align: center; font-family: "Montserrat", sans-serif; font-weight: 900; color: var(--ink); }
  .brand-dot { border-radius: 50%; background: var(--ink); }
  .brand-name { line-height: 1; letter-spacing: .02em; }
  .brand-sub { line-height: 1.1; letter-spacing: .04em; }
  .brand.on-orange .brand-dot { background: var(--black); }

  /* Business card front */
  .card-front { left: 58px; top: 78px; width: 422px; height: 241px; background: var(--white); }
  .card-front .divider { left: 210px; top: 64px; width: 1px; height: 112px; background: #777; }
  .card-name { left: 223px; top: 62px; font-family: "Arimo", sans-serif; font-weight: 700; font-size: 16px; color: var(--orange); letter-spacing: .01em; }
  .card-address { left: 223px; top: 90px; font-family: "Arimo", sans-serif; font-size: 11.5px; line-height: 14.5px; color: var(--grey-text); }
  .contact-list { left: 223px; top: 130px; font-family: "Arimo", sans-serif; font-size: 11.5px; line-height: 16.8px; color: var(--grey-text); list-style: none; }
  .contact-list li { display: flex; align-items: center; gap: 4px; }
  .contact-list svg { width: 10px; height: 10px; flex: none; }

  /* Services back card */
  .card-back { left: 511px; top: 78px; width: 422px; height: 241px; background: var(--black); }
  .card-back .top-band { left: 0; top: 0; width: 422px; height: 115px; background: var(--orange); }
  .tab { position: absolute; background: var(--black); color: var(--white); font-family: "Montserrat", sans-serif; font-weight: 900; text-align: center; }
  .card-back .tab { left: 111px; top: 100px; width: 200px; height: 30px; border-radius: 16px 16px 0 0; font-size: 20px; line-height: 32px; }
  .tagline { position: absolute; width: 100%; text-align: center; font-family: "Poppins", sans-serif; color: var(--white); letter-spacing: .08em; }
  .card-back .tagline { top: 131px; font-size: 11.5px; line-height: 17px; }
  .services { position: absolute; display: flex; justify-content: center; }
  .service { display: flex; flex-direction: column; align-items: center; color: var(--white); font-family: "Poppins", sans-serif; font-weight: 700; text-align: center; letter-spacing: .06em; }
  .service-sep { background: var(--orange); width: 2px; }
  .card-back .services { left: 0; top: 168px; width: 422px; }
  .card-back .service { width: 93px; font-size: 8px; line-height: 10px; }
  .card-back .service svg { width: 58px; height: 30px; margin-bottom: 4px; }
  .card-back .service-sep { height: 57px; margin-top: 0; }

  /* Letterhead */
  .letterhead { left: 58px; top: 357px; width: 453px; height: 641px; background: var(--white); }
  .lh-contact { left: 333px; top: 24px; font-family: "Arimo", sans-serif; font-size: 6.4px; line-height: 9.6px; color: var(--grey-text); list-style: none; }
  .lh-contact li { display: flex; align-items: center; gap: 3px; }
  .lh-contact svg { width: 6px; height: 6px; }
  .lh-rule { left: 24px; top: 77px; width: 404px; height: 1px; background: #999; }
  .letter { left: 40px; top: 196px; width: 378px; font-family: "Arimo", sans-serif; color: #3d3d3d; }
  .salutation { font-family: "Poppins", sans-serif; font-weight: 600; font-size: 10.5px; margin-bottom: 14px; }
  .letter p { font-size: 7.4px; line-height: 9.3px; margin-bottom: 8px; }
  .closing { font-family: "Poppins", sans-serif; font-weight: 600; font-size: 5.8px; margin-top: 14px; }
  .signature { margin-top: 12px; width: 76px; height: 22px; background: linear-gradient(90deg, #e9e9e9, #d5d5d5); border-radius: 3px; }

  /* Swoosh footer shared */
  .swoosh { position: absolute; left: 0; bottom: 0; }

  /* Flyer */
  .flyer { left: 546px; top: 357px; width: 387px; height: 774px; background: var(--black); }
  .roof-photo { left: 0; top: 0; width: 387px; height: 130px; background: linear-gradient(120deg, #0f3a3a 0%, #6fa3a2 35%, #1d4f4f 55%, #9cc4c2 75%, #0d3030 100%); }
  .logo-arc { left: 226px; top: -40px; width: 200px; height: 177px; border-radius: 0 0 0 100%; background: var(--orange); border-left: 3px solid var(--black); border-bottom: 3px solid var(--black); }
  .headline-band { left: 0; top: 130px; width: 387px; height: 124px; background: linear-gradient(90deg, #b8b8b8 0%, #f4f4f4 30%, #e6e6e6 60%, #bdbdbd 100%); }
  .headline { width: 100%; top: 138px; text-align: center; font-family: "Montserrat", sans-serif; font-weight: 900; font-size: 30px; line-height: 36px; color: var(--black); }
  .house-photo { left: 0; top: 254px; width: 387px; height: 212px; background: linear-gradient(180deg, #c9d3dc 0%, #8c8a82 40%, #6d6a5e 70%, #5c8a3e 100%); }
  .flyer .tab { left: 50px; top: 448px; width: 286px; height: 37px; border-radius: 19px; background: var(--orange); color: var(--black); border: 2px solid var(--black); font-size: 30px; line-height: 35px; }
  .flyer .tagline { top: 490px; font-size: 14.5px; line-height: 21px; }
  .flyer .services { left: 0; top: 537px; width: 387px; }
  .flyer .service { width: 116px; font-size: 10.5px; line-height: 12.5px; }
  .flyer .service svg { width: 72px; height: 38px; margin-bottom: 8px; }
  .flyer .service-sep { height: 74px; }
  .call-line { top: 639px; height: 1.5px; width: 66px; background: var(--white); }
  .call-pill { left: 103px; top: 625px; width: 180px; height: 31px; border-radius: 16px; background: var(--orange); font-family: "Poppins", sans-serif; font-weight: 700; font-size: 21px; line-height: 32px; text-align: center; color: var(--black); }
  .phone-big { top: 658px; width: 100%; text-align: center; font-family: "Montserrat", sans-serif; font-weight: 900; font-size: 41px; color: #ececec; letter-spacing: -.01em; }
  .web-footer { bottom: 8px; width: 100%; text-align: center; font-family: "Poppins", sans-serif; font-weight: 700; font-size: 14px; letter-spacing: .28em; color: var(--black); }
</style>
</head>
<body>
<main class="canvas">

  <!-- Business card front -->
  <section class="piece card-front" aria-label="Business card front">
    <div class="brand" style="left:40px;top:62px;width:130px;">
      <span class="brand-dot" style="width:46px;height:46px;margin-bottom:8px;"></span>
      <span class="brand-name" style="font-size:20px;">BRENMAR</span>
      <span class="brand-sub" style="font-size:6.6px;margin-top:3px;">ROOFING &amp; RENOVATIONS</span>
    </div>
    <div class="abs divider"></div>
    <h2 class="abs card-name">DANA WHITFIELD</h2>
    <p class="abs card-address">P.O. Box 5126<br>Seguin, TX 78155</p>
    <ul class="abs contact-list">
      <li><svg viewBox="0 0 10 10"><path d="M2 1l2 2-1 1.3a6 6 0 0 0 2.7 2.7L7 6l2 2-1.2 1.3C4.5 9 1 5.5.7 2.2z" fill="none" stroke="#ff8200" stroke-width="1"/></svg>830-555-0148</li>
      <li><svg viewBox="0 0 10 10"><rect x=".8" y="2" width="8.4" height="6" fill="none" stroke="#ff8200" stroke-width="1"/><path d="M.8 2L5 5.3 9.2 2" fill="none" stroke="#ff8200" stroke-width="1"/></svg>office@brenmarroofingtx.com</li>
      <li><svg viewBox="0 0 10 10"><circle cx="5" cy="5" r="4.2" fill="none" stroke="#ff8200"/><ellipse cx="5" cy="5" rx="1.8" ry="4.2" fill="none" stroke="#ff8200" stroke-width=".8"/><path d="M.8 5h8.4" stroke="#ff8200" stroke-width=".8"/></svg>www.brenmarroofingtx.com</li>
    </ul>
    <svg class="swoosh" width="422" height="60" viewBox="0 0 422 60">
      <path d="M0 48 Q210 70 422 22 V60 H0 Z" fill="#111111"/>
      <path d="M70 51 Q260 60 422 8 V17 Q250 66 70 51 Z" fill="#ff8200"/>
    </svg>
  </section>

  <!-- Business card back -->
  <section class="piece card-back" aria-label="Business card back">
    <div class="abs top-band"></div>
    <div class="brand on-orange" style="left:86px;top:24px;width:250px;flex-direction:row;justify-content:center;gap:10px;">
      <span class="brand-dot" style="width:52px;height:52px;"></span>
      <span style="display:flex;flex-direction:column;align-items:flex-start;">
        <span class="brand-name" style="font-size:28px;">BRENMAR</span>
        <span class="brand-sub" style="font-size:8.5px;margin-top:3px;">ROOFING &amp; RENOVATIONS</span>
      </span>
    </div>
    <div class="tab">OUR SERVICES</div>
    <p class="tagline">A total solutions partner for all your home<br>improvements needs</p>
    <div class="services">
      <div class="service">
        <svg viewBox="0 0 58 30"><path d="M2 24 L14 13 L22 20 L29 8 L36 20 L44 13 L56 24" fill="none" stroke="#ff8200" stroke-width="3.5" stroke-linejoin="round"/><rect x="26" y="15" width="6" height="6" fill="#ff8200"/></svg>
        ROOFING
      </div>
      <div class="service-sep"></div>
      <div class="service">
        <svg viewBox="0 0 58 30"><path d="M29 1 L47 29 H11 Z" fill="#ff8200"/><path d="M23 17 L35 25 M30 14 L36 18" stroke="#111" stroke-width="3"/></svg>
        TURN<br>SERVICES
      </div>
      <div class="service-sep"></div>
      <div class="service">
        <svg viewBox="0 0 58 30"><circle cx="29" cy="15" r="13" fill="none" stroke="#ff8200" stroke-width="2" stroke-dasharray="30 6"/><path d="M20 16 L29 8 L38 16 M23 14 V23 H35 V14 M27 23 V18 H31 V23" fill="none" stroke="#ff8200" stroke-width="2"/></svg>
        RENOVATIONS
      </div>
    </div>
  </section>

  <!-- Letterhead -->
  <section class="piece letterhead" aria-label="Letterhead">
    <div class="brand" style="left:26px;top:20px;width:76px;">
      <span class="brand-dot" style="width:34px;height:34px;margin-bottom:6px;"></span>
      <span class="brand-name" style="font-size:11.5px;">BRENMAR</span>
      <span class="brand-sub" style="font-size:4px;margin-top:2px;">ROOFING &amp; RENOVATIONS</span>
    </div>
    <ul class="abs lh-contact">
      <li>P.O. Box 5126</li>
      <li>Seguin, TX 78155</li>
      <li><svg viewBox="0 0 10 10"><path d="M2 1l2 2-1 1.3a6 6 0 0 0 2.7 2.7L7 6l2 2-1.2 1.3C4.5 9 1 5.5.7 2.2z" fill="#ff8200"/></svg>830-555-0148</li>
      <li><svg viewBox="0 0 10 10"><rect x=".8" y="2" width="8.4" height="6" fill="none" stroke="#ff8200"/><path d="M.8 2L5 5.3 9.2 2" fill="none" stroke="#ff8200"/></svg>office@brenmarroofingtx.com</li>
      <li><svg viewBox="0 0 10 10"><circle cx="5" cy="5" r="4.2" fill="#ff8200"/></svg>www.brenmarroofingtx.com</li>
    </ul>
    <div class="abs lh-rule"></div>
    <article class="abs letter">
      <p class="salutation">Dear Mr. Smith,</p>
      <p>Lorem ipsum dolor sit amet, consectetuer adipiscing elit, sed diam nonummy nibh euismod tincidunt ut laoreet dolore magna aliquam erat volutpat. Ut wisi enim ad minim veniam, quis nostrud exerci tationmcorper suscipit lobortis nisl ut aliquip ex ea commodo consequat. Duis autem vel eum iriure dolor in hendrerit in vulputate velit esse molestie consequat, vel illum dolore eu feugiat</p>
      <p>Rorem ipsum dolor sit amet, consectetuer adipiscing elit, sed diam nonummy nibh euismod tincidunt ut laoreet dolore magna aliquam erat volutpat. Ut wisi enim ad minim veniam, quis nostrud exerci tationmcorper suscipit lobortis nisl ut aliquip ex ea commodo consequat. Duis autem vel eum iriure dolor in hendrerit in vulputate velit esse molest</p>
      <p>Dorem ipsum dolor sit amet, consectetuer adipiscing elit, sed diam nonummy nibh euismod tincidunt ut laoreet dolore magna aliquam erat volutpat. Ut wisi enim ad minim veniam, quis nostrud exerci tationmcorper suscipit lobortis nisl ut aliquip ex ea commodo consequat. Duis autem vel eum iriure dolor in hendrerit in suscipit lobortis nisl ut aliquip ex ea commodo consequat. Duis autem vel eum iriure dolor in hendrerit in vulputate velit esse molestie consequat, vel illum</p>
      <p>Sorem ipsum dolor sit amet, consectetuer adipiscing elit, sed diam nonummy nibh euismod tincidunt ut laoreet dolore magna aliquam erat volutpat. Ut wisi enim ad minim veniam, quis nostrud exerci tationmcorper suscipit lobortis nisl ut aliquip ex ea commodo consequat. Duis autem vel eum iriure dolor in</p>
      <p class="closing">Sincerely,</p>
      <div class="signature" role="img" aria-label="Handwritten signature"></div>
    </article>
    <svg class="swoosh" width="453" height="62" viewBox="0 0 453 62">
      <path d="M0 44 Q230 74 453 22 V62 H0 Z" fill="#111111"/>
      <path d="M70 48 Q280 62 453 4 V16 Q260 68 70 48 Z" fill="#ff8200"/>
    </svg>
  </section>

  <!-- Flyer -->
  <section class="piece flyer" aria-label="Rack card flyer">
    <div class="abs roof-photo" role="img" aria-label="Close-up photo of glossy teal metal roof tiles"></div>
    <div class="abs logo-arc"></div>
    <div class="brand" style="left:262px;top:14px;width:120px;">
      <span class="brand-dot" style="width:48px;height:48px;margin-bottom:10px;"></span>
      <span class="brand-name" style="font-size:18px;">BRENMAR</span>
      <span class="brand-sub" style="font-size:5.6px;margin-top:2px;">ROOFING &amp; RENOVATIONS</span>
    </div>
    <div class="abs headline-band"></div>
    <h1 class="abs headline">LOCAL ROOFING<br>COMPANY SERVING<br>GREATER, TX</h1>
    <div class="abs house-photo" role="img" aria-label="Photo of a large two-storey suburban house with a brown shingle roof and landscaped front yard"></div>
    <div class="tab">OUR SERVICES</div>
    <p class="tagline">A total solutions partner for all your home<br>improvements needs</p>
    <div class="services">
      <div class="service">
        <svg viewBox="0 0 58 30"><path d="M2 24 L14 13 L22 20 L29 8 L36 20 L44 13 L56 24" fill="none" stroke="#ff8200" stroke-width="3.5" stroke-linejoin="round"/><rect x="26" y="15" width="6" height="6" fill="#ff8200"/></svg>
        ROOFING
      </div>
      <div class="service-sep"></div>
      <div class="service">
        <svg viewBox="0 0 58 30"><path d="M29 1 L47 29 H11 Z" fill="#ff8200"/><path d="M23 17 L35 25 M30 14 L36 18" stroke="#111" stroke-width="3"/></svg>
        TURN<br>SERVICES
      </div>
      <div class="service-sep"></div>
      <div class="service">
        <svg viewBox="0 0 58 30"><circle cx="29" cy="15" r="13" fill="none" stroke="#ff8200" stroke-width="2" stroke-dasharray="30 6"/><path d="M20 16 L29 8 L38 16 M23 14 V23 H35 V14 M27 23 V18 H31 V23" fill="none" stroke="#ff8200" stroke-width="2"/></svg>
        RENOVATIONS
      </div>
    </div>
    <div class="abs call-line" style="left:31px;"></div>
    <div class="abs call-pill">Call Us Today</div>
    <div class="abs call-line" style="left:290px;"></div>
    <p class="abs phone-big">830-555-0148</p>
    <svg class="swoosh" width="387" height="80" viewBox="0 0 387 80">
      <defs>
        <linearGradient id="silver" x1="0" x2="1">
          <stop offset="0" stop-color="#555"/><stop offset=".6" stop-color="#f2f2f2"/><stop offset="1" stop-color="#9a9a9a"/>
        </linearGradient>
      </defs>
      <path d="M0 28 Q200 50 387 10 V20 Q200 58 0 34 Z" fill="url(#silver)"/>
      <path d="M0 34 Q200 58 387 20 V80 H0 Z" fill="#ff8200"/>
      <path d="M0 34 Q200 58 387 20 V24 Q200 62 60 44 Q20 40 0 38 Z" fill="#111111"/>
    </svg>
    <p class="abs web-footer">www.brenmarroofingtx.com</p>
  </section>

</main>
</body>
</html>
```